Yoga Studio Postcard Advertising Flyer

Need a postcard size flyer that will promote our business. The objective is to promote location and availability. Want it to be personal. The objective to connect the audience to the purpose of yoga and the focus on enabling functional well-being. Something that is a very big focus at this point in time in the world. I really want people to see the value in connecting with us via our website, classora app, linkhive or pixly. The colours are to be bright but not overwhelming and aligned to the logo colours. Its also important to have the location picture on the flyer - unless you think that it is way too much (try a with or without). I don't want this to be a specials brochure - it is an introduction to our brand and our business. No need to over do it with promotional lines apart from come and join us.
Updates

Delayed in organising this.

Target Market(s)

Local yogis and residence who are or want to be focused on well-being.

Requirements
Must have
• Pictures - would have the logo on one side.
Nice to have
• Modern and aligned to website design.

```html
<!DOCTYPE html>
<html lang="en">
<head>
<meta charset="utf-8">
<title>Crane Lily Yoga – Postcard</title>
<link rel="stylesheet" href="https://fonts.googleapis.com/css2?family=Roboto+Condensed:wght@300;400&family=Source+Sans+3:wght@400;600;700&display=swap">
<style>
  :root{
    --navy:#14264f;
    --navy-deep:#0c1a3a;
    --sky:#29a3dc;
    --sky-light:#bfe0f4;
    --ink:#3d3d3d;
    --paper:#ffffff;
    --backdrop:#e9eaec;
    --figure:#d7dde8;
  }
  *{box-sizing:border-box;margin:0;padding:0}
  html,body{width:974px;height:1200px;overflow:hidden;background:var(--backdrop)}
  .sheet{position:relative;width:974px;height:1200px}
  .card{position:absolute;left:175px;width:700px;height:500px;background:var(--paper);
    transform:scale(0.891);transform-origin:top left;overflow:hidden;
    box-shadow:0 2px 6px rgba(0,0,0,.18);font-family:"Source Sans 3",sans-serif}
  .card--front{top:140px}
  .card--back{top:628px}
  .card svg.shapes{position:absolute;inset:0}
  .brand{position:absolute;text-align:center;font-family:"Roboto Condensed",sans-serif;
    font-weight:400;color:var(--navy);font-size:25px;letter-spacing:.5px;line-height:1}
  .brand::before{content:"";display:block;width:34px;height:34px;border-radius:50%;
    background:var(--sky);margin:0 auto 14px}
  .card--front .brand{left:27px;top:68px;width:200px}
  .card--back .brand{left:250px;top:28px;width:200px}
  .headline{position:absolute;left:33px;top:270px;font-family:"Roboto Condensed",sans-serif;
    font-weight:400;font-size:25px;line-height:30px;color:var(--navy)}
  .headline::after{content:"";display:block;width:130px;height:2px;background:var(--sky);margin-top:7px}
  .benefits{position:absolute;left:31px;top:348px;width:330px;list-style:none;
    font-size:13px;line-height:13.5px;color:var(--ink)}
  .benefits li{position:relative;padding-left:23px;margin-bottom:6px}
  .benefits li::before{content:"";position:absolute;left:0;top:1px;width:12px;height:12px;
    border-radius:50%;background:var(--sky)}
  .benefits li::after{content:"";position:absolute;left:3.5px;top:3.5px;width:5px;height:3px;
    border-left:1.5px solid #fff;border-bottom:1.5px solid #fff;transform:rotate(-45deg)}
  .address{position:absolute;left:36px;top:462px;display:flex;align-items:center;gap:10px;
    font-size:12.5px;font-weight:600;color:var(--navy-deep)}
  .socials{position:absolute;right:17px;top:385px;display:flex;gap:8px;font-size:11px;color:#fff}
  .socials span{display:flex;align-items:center;gap:3px}
  .socials span::before{content:"";width:9px;height:9px;background:var(--sky)}
  .cta{position:absolute;right:17px;top:416px;font-family:"Roboto Condensed",sans-serif;
    font-weight:300;font-size:26px;color:#fff;letter-spacing:.3px}
  .web{position:absolute;left:462px;top:455px;width:238px;height:27px;background:var(--sky);
    display:flex;align-items:center;gap:7px;padding-left:33px;font-size:12.5px;font-weight:700;color:#fff}
  .section-title{position:absolute;left:0;width:700px;top:147px;text-align:center;
    font-family:"Source Sans 3",sans-serif;font-weight:600;font-size:17px;letter-spacing:1.5px;color:var(--sky)}
  .pose{position:absolute;width:120px;text-align:center;font-size:11.5px;line-height:13px;color:#555}
  .pose .figure{display:block;width:34px;height:60px;margin:0 auto 6px;border-radius:8px;background:var(--figure)}
  .pose .figure.wide{width:84px;height:44px;margin-top:16px}
</style>
</head>
<body>
<main class="sheet">

  <section class="card card--front">
    <svg class="shapes" viewBox="0 0 700 500" width="700" height="500">
      <defs>
        <linearGradient id="skyPhoto" x1="0" y1="0" x2="0" y2="1">
          <stop offset="0" stop-color="#5fa3d6"/>
          <stop offset=".55" stop-color="#b9d7ea"/>
          <stop offset=".8" stop-color="#b9976e"/>
          <stop offset="1" stop-color="#8f7656"/>
        </linearGradient>
        <radialGradient id="navyGlow" cx=".6" cy=".3" r=".8">
          <stop offset="0" stop-color="#1d3e7a"/>
          <stop offset="1" stop-color="#0c1a3a"/>
        </radialGradient>
      </defs>
      <rect width="700" height="500" fill="url(#skyPhoto)" role="img" aria-label="Photo of a man holding a warrior yoga pose on a seaside rock platform"/>
      <path d="M0,225 C100,200 220,195 300,235 C350,262 388,305 395,340 L333,500 L0,500 Z" fill="var(--paper)"/>
      <path d="M395,340 C480,380 610,370 700,290 L700,500 L333,500 Z" fill="url(#navyGlow)"/>
      <path d="M395,340 C480,385 620,372 700,252 L700,290 C610,370 480,380 395,340 Z" fill="var(--sky)"/>
      <path d="M230,214 C300,225 360,290 395,340" fill="none" stroke="var(--sky)" stroke-width="1.5"/>
    </svg>

    <div class="brand">Crane Lily Yoga</div>

    <h1 class="headline">ENABLE FUNCTIONAL<br>WELL-BEING</h1>
    <ul class="benefits">
      <li>Strengthen your well-being through adaptive yoga.</li>
      <li>Seek to evolve your mind and body through the challenge of yoga.</li>
      <li>Perfection is a desire and never an outcome through the practice of yoga.</li>
    </ul>

    <p class="address">
      <svg width="13" height="18" viewBox="0 0 13 18" aria-hidden="true">
        <path d="M6.5 0C2.9 0 0 2.8 0 6.3 0 11 6.5 18 6.5 18S13 11 13 6.3C13 2.8 10.1 0 6.5 0Z" fill="var(--sky)"/>
        <circle cx="6.5" cy="6.3" r="2.4" fill="#fff"/>
      </svg>
      The Hall, 212 Harbour Lane Seaview NSW 2100
    </p>

    <div class="socials"><span>linkhive</span><span>classora</span><span>pixly</span></div>
    <p class="cta">COME JOIN US!</p>
    <p class="web">
      <svg width="11" height="11" viewBox="0 0 12 12" aria-hidden="true" fill="none" stroke="#fff" stroke-width="1">
        <circle cx="6" cy="6" r="5.3"/><ellipse cx="6" cy="6" rx="2.3" ry="5.3"/><path d="M.7 6h10.6"/>
      </svg>
      www.cranelilyyoga.com.au
    </p>
  </section>

  <section class="card card--back">
    <div class="brand">Crane Lily Yoga</div>
    <h2 class="section-title">SUN SALUTATION</h2>

    <div class="pose" style="left:54px;top:188px"><span class="figure" role="img" aria-label="Standing pose figure"></span>Tadasana</div>
    <div class="pose" style="left:230px;top:188px"><span class="figure" role="img" aria-label="Arms raised pose figure"></span>Utthitta<br>Tadasana</div>
    <div class="pose" style="left:392px;top:188px"><span class="figure" role="img" aria-label="Forward fold pose figure"></span>Uttanasana</div>
    <div class="pose" style="left:566px;top:188px"><span class="figure" role="img" aria-label="Half forward fold pose figure"></span>Ardha<br>Uttanasana</div>

    <div class="pose" style="left:54px;top:282px"><span class="figure wide" role="img" aria-label="Plank pose figure"></span>Chaturanga<br>Dandasana</div>
    <div class="pose" style="left:230px;top:282px"><span class="figure wide" role="img" aria-label="Upward dog pose figure"></span>Urdhva Mukha<br>Svanasana</div>
    <div class="pose" style="left:394px;top:282px"><span class="figure wide" role="img" aria-label="Downward dog pose figure"></span>Adho Mukha<br>Svanasana</div>
    <div class="pose" style="left:566px;top:282px"><span class="figure" role="img" aria-label="Half forward fold pose figure"></span>Ardha<br>Uttanasana</div>

    <div class="pose" style="left:138px;top:378px"><span class="figure" role="img" aria-label="Forward fold pose figure"></span>Uttanasana</div>
    <div class="pose" style="left:312px;top:378px"><span class="figure" role="img" aria-label="Arms raised pose figure"></span>Utthitta<br>Tadasana</div>
    <div class="pose" style="left:496px;top:378px"><span class="figure" role="img" aria-label="Standing pose figure"></span>Tadasana</div>
  </section>

</main>
</body>
</html>
```